Offshore Energy Projects Management Consultancy needs a business card design

Logo available. We provide teams to deliver engineering consultancy, project management and delivery teams mainly in the offshore renewables sector. The company is all about bringing the right people to a project to deliver the scope.

The business card will be used for all staff.

The business card should be quite simple, vibrant and uncluttered but convey experience, enthusiasm and integration.

Target Market(s)

Energy Project Developers and Tier 1 construction companies

Contact Information for Business Card

Logo should be on the back of the card. I'm happy for the designer to play with the colour of the logo and background colour.

Front of the card should convey all the must have information in a clear and professional manner but without being overly traditional.

Colors

Designer to choose colors to be used in the design.

Requirements
Must have
• Land Line Tel Number, Mobile Tel Number, Email, business address, web address.

```html
<!DOCTYPE html>
<html lang="en">
<head>
<meta charset="utf-8">
<title>Tidewell Project Partners – Business Card</title>
<link rel="stylesheet" href="https://fonts.googleapis.com/css2?family=Exo+2:wght@300;400;600;700&display=swap">
<style>
  :root {
    --page-bg: #dcd8d2;
    --card-white: #f4f4f4;
    --brand-blue: #1169b0;
    --brand-blue-light: #2a9fd8;
    --panel-grey: #646569;
    --text-dark: #3a3a3c;
    --back-dark: #242325;
    --white: #ffffff;
  }
  * { margin: 0; padding: 0; box-sizing: border-box; }
  html, body { width: 900px; height: 1200px; overflow: hidden; }
  body {
    background: var(--page-bg);
    position: relative;
    font-family: "Exo 2", Arial, sans-serif;
  }
  .card {
    position: absolute;
    border-radius: 22px;
    overflow: hidden;
    box-shadow: 0 6px 16px rgba(0,0,0,0.25);
  }
  .card-front { left: 78px; top: 136px; width: 762px; height: 434px; background: var(--card-white); }
  .card-back  { left: 76px; top: 630px; width: 767px; height: 435px; background: var(--back-dark); }

  .front-panels { position: absolute; inset: 0; }

  .brand-front {
    position: absolute; left: 48px; top: 72px; width: 250px;
    display: flex; align-items: center; gap: 10px;
    color: var(--brand-blue);
    font-weight: 700; font-size: 22px; line-height: 1.15;
    letter-spacing: 0.3px; text-transform: uppercase;
  }
  .brand-dot { width: 18px; height: 18px; border-radius: 50%; background: var(--brand-blue); flex: none; }

  .holder {
    position: absolute; right: 42px; top: 72px; text-align: right; color: var(--white);
  }
  .holder-name { font-weight: 600; font-size: 28px; letter-spacing: 0.3px; line-height: 1; }
  .holder-role { font-weight: 300; font-size: 24px; line-height: 1.1; }

  .address {
    position: absolute; right: 46px; top: 342px; text-align: right;
    color: var(--white); font-size: 19px; line-height: 26px; font-weight: 400; font-style: normal;
  }

  .contact-list { position: absolute; left: 42px; list-style: none; color: var(--text-dark); font-size: 19px; }
  .contact-list li { display: flex; align-items: center; height: 27px; }
  .contact-list svg { width: 22px; height: 22px; margin-right: 14px; fill: var(--brand-blue-light); }
  .phones { top: 256px; }
  .online { top: 339px; }
  .web { font-weight: 600; }

  .brand-back {
    position: absolute; inset: 0;
    display: flex; justify-content: center; align-items: center; gap: 22px;
    color: var(--brand-blue-light);
    font-weight: 700; text-transform: uppercase; text-align: center;
  }
  .brand-back .brand-dot { width: 38px; height: 38px; background: var(--brand-blue-light); }
  .brand-back-name { font-size: 54px; line-height: 1.1; letter-spacing: 1px; }
</style>
</head>
<body>
  <section class="card card-front" aria-label="Business card front">
    <svg class="front-panels" viewBox="0 0 762 434" aria-hidden="true">
      <polygon points="284,0 762,0 762,212 388,212" fill="var(--brand-blue)"/>
      <polygon points="392,219 762,219 762,434 497,434" fill="var(--panel-grey)"/>
    </svg>

    <div class="brand-front"><span class="brand-dot"></span><span>Tidewell<br>Project Partners</span></div>

    <div class="holder">
      <div class="holder-name">MARCUS ELLERY</div>
      <div class="holder-role">owner</div>
    </div>

    <ul class="contact-list phones">
      <li><svg viewBox="0 0 24 24"><path d="M2 9c0-3 4-5 10-5s10 2 10 5v2h-5V8.5c-1.5-.6-3.2-.9-5-.9s-3.5.3-5 .9V11H2zM6 12l2-3h8l2 3v7H6zm6 1.5a2.5 2.5 0 1 0 0 5 2.5 2.5 0 0 0 0-5z"/></svg>020 555 0147</li>
      <li><svg viewBox="0 0 24 24"><path d="M7 1h10a2 2 0 0 1 2 2v18a2 2 0 0 1-2 2H7a2 2 0 0 1-2-2V3a2 2 0 0 1 2-2zm0 3v15h10V4zm5 16.2a1 1 0 1 0 0 2 1 1 0 0 0 0-2z"/></svg>020 555 0193</li>
    </ul>

    <ul class="contact-list online">
      <li><svg viewBox="0 0 24 24"><path d="M2 5h20v2l-10 6L2 7zm0 4.3l10 6 10-6V19H2z"/></svg>hello@tidewellpartners.com</li>
      <li class="web"><svg viewBox="0 0 24 24"><path d="M12 2a10 10 0 1 0 0 20 10 10 0 0 0 0-20zm0 2c.9 0 2.2 1.8 2.7 5H9.3c.5-3.2 1.8-5 2.7-5zM4.3 11h3c0 .7 0 1.4.1 2H4.3a8 8 0 0 1 0-2zm5 0h5.4a18 18 0 0 1 0 2H9.3a18 18 0 0 1 0-2zm7.4 0h3a8 8 0 0 1 0 2h-3c.1-.6.1-1.3 0-2zM9.3 15h5.4c-.5 3.2-1.8 5-2.7 5s-2.2-1.8-2.7-5zM5 9a8 8 0 0 1 3.8-4.3c-.6 1.1-1.1 2.6-1.3 4.3zm11.5 0c-.2-1.7-.7-3.2-1.3-4.3A8 8 0 0 1 19 9zM5 15h2.5c.2 1.7.7 3.2 1.3 4.3A8 8 0 0 1 5 15zm11.5 0H19a8 8 0 0 1-3.8 4.3c.6-1.1 1.1-2.6 1.3-4.3z"/></svg>www.tidewellpartners.com</li>
    </ul>

    <address class="address">27 Harbour Quay Road<br>Portwick, ME 04110</address>
  </section>

  <section class="card card-back" aria-label="Business card back">
    <div class="brand-back"><span class="brand-dot"></span><span class="brand-back-name">Tidewell<br>Project Partners</span></div>
  </section>
</body>
</html>
```